Business Card Design - Ember Hill Lodge

We are looking at a new design for our business cards that has a modern and professional look. We run a residential aged care facility focussing on the care of residents. The cards will be used for potential clients, consultants and business opportunities in this sector. Blue and white is our main colours and would to see these colours incorporated in the design.
Industry/Entity Type
Business
Contact Information for Business Card
Ember Hill Lodge, Dean Marsh, dmarsh@emberhilllodge-mail.example, Finance Manager, 0491 372 608, BCom, 27 Marbury Way, Ashgrove Vale, Qld 4312.
Look and feel

```html
<!DOCTYPE html>
<html lang="en">
<head>
<meta charset="utf-8">
<title>Ember Hill Lodge – Business Card</title>
<link rel="stylesheet" href="https://fonts.googleapis.com/css2?family=Source+Sans+3:ital,wght@0,400;0,600;1,400&display=swap">
<style>
  :root {
    --brand-blue: #4d7a94;
    --card-white: #ffffff;
    --backdrop: #e9e6e3;
    --ink-on-blue: #ffffff;
    --tagline-grey: #a39690;
  }
  * { margin: 0; padding: 0; box-sizing: border-box; }
  html, body {
    width: 1200px;
    height: 900px;
    overflow: hidden;
    background: var(--backdrop);
    font-family: "Source Sans 3", "Myriad Pro", Arial, sans-serif;
  }
  .canvas { position: relative; width: 1200px; height: 900px; }

  .card {
    position: absolute;
    background: var(--card-white);
    box-shadow: 0 6px 18px rgba(0,0,0,0.12);
    overflow: hidden;
  }

  /* Front */
  .card-front { left: 78px; top: 34px; width: 588px; height: 364px; }
  .front-brand {
    position: absolute;
    left: 34px;
    top: 124px;
    display: flex;
    align-items: center;
    gap: 8px;
  }
  .brand-dot {
    width: 18px; height: 18px;
    border-radius: 50%;
    background: var(--brand-blue);
  }
  .brand-name {
    font-weight: 400;
    font-size: 22px;
    line-height: 26px;
    letter-spacing: 1.5px;
    color: var(--brand-blue);
    text-transform: uppercase;
  }
  .front-tagline {
    position: absolute;
    left: 33px;
    top: 151px;
    width: 193px;
    height: 18px;
    background: var(--tagline-grey);
    color: var(--card-white);
    font-style: italic;
    font-size: 13px;
    line-height: 18px;
    text-align: center;
  }
  .front-band {
    position: absolute;
    left: 0; top: 182px;
    width: 100%; height: 182px;
    background: var(--brand-blue);
    color: var(--ink-on-blue);
    padding: 10px 0 0 30px;
  }
  .person-name { font-size: 21px; font-weight: 600; line-height: 28px; }
  .person-name .credential { font-size: 15px; }
  .person-role { font-size: 16px; line-height: 20px; }
  .contact-list { list-style: none; margin-top: 12px; font-size: 16px; }
  .contact-list li { display: flex; align-items: center; gap: 7px; height: 25px; }
  .contact-list svg { width: 13px; height: 13px; fill: var(--ink-on-blue); }
  .address { margin-top: 6px; font-size: 16px; }

  /* Back */
  .card-back { left: 388px; top: 505px; width: 567px; height: 352px; }
  .back-band {
    position: absolute;
    left: 0; top: 110px;
    width: 100%; height: 131px;
    background: var(--brand-blue);
  }
  .back-name {
    position: absolute;
    left: 0; right: 0;
    top: 26px;
    text-align: center;
    font-weight: 400;
    font-size: 32px;
    letter-spacing: 3px;
    color: var(--ink-on-blue);
    text-transform: uppercase;
    line-height: 36px;
  }
  .back-tagline {
    position: absolute;
    left: 127px;
    top: 68px;
    width: 313px;
    height: 31px;
    background: var(--card-white);
    color: var(--brand-blue);
    font-style: italic;
    font-size: 20px;
    line-height: 31px;
    text-align: center;
  }
</style>
</head>
<body>
<main class="canvas">
  <section class="card card-front" aria-label="Business card front">
    <div class="front-brand">
      <span class="brand-dot"></span>
      <span class="brand-name">Ember Hill Lodge</span>
    </div>
    <p class="front-tagline">Respect, Comfort, Community</p>
    <div class="front-band">
      <p class="person-name">Dean Marsh, <span class="credential">BCom</span></p>
      <p class="person-role">Finance Manager</p>
      <ul class="contact-list">
        <li>
          <svg viewBox="0 0 24 24" aria-hidden="true"><path d="M6.6 10.8a15.2 15.2 0 0 0 6.6 6.6l2.2-2.2a1 1 0 0 1 1-.25 11.4 11.4 0 0 0 3.6.57 1 1 0 0 1 1 1V20a1 1 0 0 1-1 1A17 17 0 0 1 3 4a1 1 0 0 1 1-1h3.5a1 1 0 0 1 1 1c0 1.25.2 2.45.57 3.57a1 1 0 0 1-.25 1z"/></svg>
          0491 372 608
        </li>
        <li>
          <svg viewBox="0 0 24 24" aria-hidden="true"><path d="M2 5h20v14H2z M3.5 6.5 12 13l8.5-6.5" fill="none" stroke="#fff" stroke-width="2"/></svg>
          dmarsh@emberhilllodge-mail.example
        </li>
      </ul>
      <p class="address">27 Marbury Way, Ashgrove Vale, Qld 4312</p>
    </div>
  </section>

  <section class="card card-back" aria-label="Business card back">
    <div class="back-band">
      <span class="back-name">Ember Hill Lodge</span>
      <span class="back-tagline">Respect, Comfort, Community</span>
    </div>
  </section>
</main>
</body>
</html>
```